Letterhead for 3 attorney Workers' Comp law firm

We are a 3 attorney law office. We specialize in Workers' Compensation. Our office represents workers who are injured on the job, and the estates of workers who are killed one the job.
When we started our office, we created our own letterhead & have been using it for years. We've just recently hired the 3rd attorney, and were going to just add his name to the letterhead, but have decided we wanted to get a professionally designed letterhead and business cards at this point.
We want something that looks clean and professional. It must look good in black and white because we often make multiple copies of our documents. We're hoping for a design that resonates confidence, reliability and experience.
The design must include the firm name: Dorrance & Pike, PLLC. We would like the PLLC to be small compared to the Dorrance & Pike graphic. We also want to incorporate the attorney names: Ulric Dorrance, Janet Pike, and Lyle Hagberg. Our current letterhead has our contact info in the footer at the bottom of the page. We like that design, but are open to the idea of having it at the top. We'll leave that at the discretion of the designer. Our contact info is as follows: 472 S. Larchmont Avenue, Suite 315 Bellingham, WA 98117 Phone: 360-514-2967, Fax: 360-521-6079, and our website: www.dorrancepike-law.example
Target Market(s)
Clients, courts, other legal offices, doctors offices. These are the people who see our letterhead most frequently. It's not so much for marketing purposes, mainly so that we have a professional image when sending out documents.
Industry/Entity Type
Law Firm
Contact Information for Business Card
On the back of the business card: it can be designed, or be a template for filling in appointment reminder information (i.e. date, time, etc)
Colors
Designer to choose colors to be used in the design.
Requirements
Must have
- Must have our firm name at the top.
- Must include the attorney names.
- Must have all of our contact information (can be at top or bottom - whatever looks best with the design)
Nice to have
- A strong, confident design
Should not have
- We don't want the design to be playful, cartoony or busy.

```html
<!DOCTYPE html>
<html lang="en">
<head>
<meta charset="utf-8">
<title>Dorrance &amp; Pike, PLLC — Letterhead</title>
<link href="https://fonts.googleapis.com/css2?family=Cinzel:wght@500&family=Lato:wght@400&display=swap" rel="stylesheet">
<style>
  :root {
    --backdrop: #efefef;
    --paper: #ffffff;
    --band: #414042;
    --band-text: #ffffff;
    --ink: #2b2b2b;
    --rule: #d9d9d9;
  }
  * { box-sizing: border-box; margin: 0; padding: 0; }
  html, body {
    width: 1155px;
    height: 1200px;
    overflow: hidden;
    background: var(--backdrop);
  }
  .letterhead {
    position: absolute;
    left: 126px;
    top: 0;
    width: 903px;
    height: 1200px;
    background: var(--paper);
  }
  .masthead {
    position: absolute;
    left: 0; top: 0;
    width: 100%;
    height: 141px;
    background: var(--band);
    color: var(--band-text);
  }
  .firm-name {
    position: absolute;
    left: 56px;
    top: 54px;
    font-family: "Cinzel", "Times New Roman", serif;
    font-weight: 500;
    font-size: 27px;
    letter-spacing: 0.5px;
    line-height: 1;
    white-space: nowrap;
  }
  .attorneys, .address {
    position: absolute;
    top: 57px;
    font-family: "Lato", Arial, sans-serif;
    font-size: 12.5px;
    line-height: 16px;
    list-style: none;
    font-style: normal;
  }
  .attorneys { left: 571px; }
  .divider {
    position: absolute;
    left: 667px;
    top: 58px;
    width: 1px;
    height: 46px;
    background: var(--band-text);
    opacity: 0.8;
  }
  .address { left: 690px; }
  .contact-bar {
    position: absolute;
    left: 0;
    width: 100%;
    top: 1156px;
    display: flex;
    justify-content: center;
    gap: 18px;
    font-family: "Lato", Arial, sans-serif;
    font-size: 15px;
    color: var(--ink);
  }
  .contact-item { display: flex; align-items: center; gap: 6px; }
  .contact-item svg { width: 12px; height: 12px; fill: none; stroke: var(--ink); stroke-width: 1.6; }
  .contact-item .solid { fill: var(--ink); stroke: none; }
</style>
</head>
<body>
  <main class="letterhead">
    <header class="masthead">
      <h1 class="firm-name">Dorrance &amp; Pike, PLLC</h1>
      <ul class="attorneys">
        <li>Ulric Dorrance</li>
        <li>Janet Pike</li>
        <li>Lyle Hagberg</li>
      </ul>
      <span class="divider"></span>
      <address class="address">
        472 S. Larchmont Avenue,<br>
        Suite 315 Bellingham,<br>
        WA 98117
      </address>
    </header>

    <footer class="contact-bar">
      <span class="contact-item">
        <svg viewBox="0 0 12 12" aria-hidden="true"><path class="solid" d="M2.2 1 L4.4 3.2 L3.4 4.6 C4.2 6.2 5.6 7.6 7.3 8.5 L8.7 7.5 L11 9.7 L9.7 11 C5.3 10.6 1.3 6.7 1 2.3 Z"/></svg>
        360-514-2967
      </span>
      <span class="contact-item">
        <svg viewBox="0 0 12 12" aria-hidden="true"><rect x="3" y="1.5" width="6" height="3"/><rect x="1" y="4.5" width="10" height="4.5" class="solid"/><rect x="3" y="8" width="6" height="3"/></svg>
        360-521-6079
      </span>
      <span class="contact-item">
        <svg viewBox="0 0 12 12" aria-hidden="true"><circle cx="6" cy="6" r="5"/><ellipse cx="6" cy="6" rx="2.2" ry="5"/><path d="M1 6 H11"/></svg>
        www.dorrancepike-law.example
      </span>
    </footer>
  </main>
</body>
</html>
```